Redesign of existing Web Design Project

I wish to redsesign the web pages on www.qbrl.com.au

Background of Harlowe Bexley

Harlowe Bexley Construction Services was established in 2004 as a boutique construction company offering construction advice and management services. We assist people in the construction minefield – step by step.

We offer services in: -

• Construction Management
• Project Management
• Building

The essence of our business is ensuring every project we undertake achieves the client’s objectives. Our experience has shown the secrets to a profitable project are -

• Planning
• Attention to detail
• Value add

We take the trouble to understand the client’s needs in person. Our hands-on approach ensures those involved deliver to the required quality standards at the scheduled times.

Our area of works include: -

• Residential single and multistorey developments
• Education facilities
• Suburban commercial building and refurbishment
• Health
• Defence
• Industrial

Objective of Acquisition

We are planning to expand our business activities. We are aiming to increase our turnover and use website as an increased passive selling tool.

Possible company type

This is an ideal opportunity for person who can capture readers attention.

Target Market(s)

see www.qbrl.com.au

Industry/Entity Type

Construction

Requirements
Must have
• Capture peoples attention on readers zones

```html
<!DOCTYPE html>
<html lang="en">
<head>
<meta charset="utf-8">
<title>Harlowe Bexley Construction Services</title>
<link rel="stylesheet" href="https://fonts.googleapis.com/css2?family=Arimo:ital,wght@0,400;0,700;1,400&family=Roboto+Condensed:wght@400&display=swap">
<style>
:root{
  --bg-top:#e9ebed;
  --bg-main:#f5f6f8;
  --navy:#3b4f77;
  --teal-dark:#2e5d6e;
  --teal-deep:#0f3442;
  --ink:#1d2a33;
  --text:#333a40;
  --muted:#6a7075;
  --rule:#22343f;
  --head-grad-a:#ffffff;
  --head-grad-b:#d8dfe8;
  --quote-bg:#e4e8ef;
  --tick:#6aa63a;
}
*{margin:0;padding:0;box-sizing:border-box}
html,body{width:1092px;height:1200px;overflow:hidden}
body{position:relative;background:var(--bg-main);font-family:Arimo,Arial,sans-serif;color:var(--text)}
.top-band{position:absolute;left:0;top:0;width:1092px;height:560px;background:var(--bg-top)}
.abs{position:absolute}

/* brand */
.brand{left:145px;top:58px;display:flex;align-items:center;gap:12px}
.brand-mark{width:40px;height:40px;background:var(--navy)}
.brand-name{font-size:27px;font-weight:700;color:var(--navy);line-height:1.1}

/* nav */
.nav-rule{left:145px;top:136px;width:802px;height:4px;background:var(--rule)}
.nav-rule::before{content:"";position:absolute;left:0;top:0;width:70px;height:4px;background:#8a9aa4}
.nav{left:145px;top:140px;width:802px;height:37px;background:linear-gradient(#f7f8fa,#dfe4ea);border-bottom:1px solid #fff}
.nav a{position:absolute;top:0;height:37px;line-height:32px;font-size:11.5px;color:#3b4650;text-decoration:none;letter-spacing:.3px}
.nav a.current{left:1px;width:68px;top:3px;height:33px;background:var(--teal-dark);color:#fff;text-align:center;line-height:30px}
.search{left:602px;top:9px;width:191px;height:20px;background:#fff;border:1px solid #c9d0d6;font-size:10px;font-style:italic;color:#98a0a6;padding:3px 8px}
.search svg{position:absolute;right:5px;top:3px}

/* hero */
.hero-shadow{left:90px;top:500px;width:920px;height:34px;background:radial-gradient(ellipse at center,rgba(0,0,0,.28),rgba(0,0,0,0) 70%)}
.hero{left:143px;top:188px;width:807px;height:343px;overflow:hidden;background:linear-gradient(180deg,#aabccd 0%,#7f97ad 45%,#5b6b77 75%,#8d9aa3 100%)}
.service{position:absolute;left:0;width:305px;height:114px;padding:20px 7px 0 20px;color:#e8f0f3}
.service h3{font-weight:400;font-size:15.5px;color:#fff;margin-bottom:6px;letter-spacing:-.2px}
.service p{font-size:10.5px;line-height:15.5px;text-align:justify;color:#dbe6ea}
.service .more{color:#bcd2da;margin-left:30px}
.s1{top:0;background:rgba(108,146,160,.82)}
.s2{top:114px;background:rgba(72,118,134,.84)}
.s3{top:228px;height:115px;background:rgba(50,96,112,.86)}
.feature{position:absolute;left:432px;top:154px;width:363px;height:175px;background:rgba(12,48,62,.93);padding:6px 10px;color:#fff}
.feature h1{font-family:"Roboto Condensed",Arial,sans-serif;font-weight:400;font-size:28px;line-height:33px;margin-bottom:12px}
.feature p{font-size:10.5px;line-height:15.5px;text-align:justify}
.feature .more{display:block;text-align:right;color:#a9c3cc;margin-top:11px;margin-right:10px;font-size:10.5px}

/* section heads */
.sec-head{height:23px;background:linear-gradient(var(--head-grad-a),var(--head-grad-b));border-top:1px solid #fff;padding:2px 4px;font-size:16px;color:var(--ink);font-weight:400}
.sec-head b{font-weight:700}
.welcome-head{left:145px;top:583px;width:359px}
.testi-head{left:588px;top:583px;width:358px}
.exp-head{left:588px;top:769px;width:358px}

.intro{left:145px;top:619px;width:360px;font-size:10.3px;line-height:15.5px;color:#2a3238}
.why{left:145px;top:685px;font-size:14px;color:#39434b}
.reasons{left:160px;top:715px;width:346px;list-style:none}
.reasons li{position:relative;padding-left:36px;font-size:10.3px;line-height:12px;color:#2f363c;margin-bottom:12px}
.reasons li svg{position:absolute;left:2px;top:0}

.quote{left:588px;top:615px;width:358px;height:99px;background:var(--quote-bg);padding:4px 8px;font-style:italic;font-size:10.3px;line-height:15.5px;color:#2f363c}
.quote-tail{left:805px;top:713px}
.signature{left:588px;top:735px;width:358px;text-align:right;font-size:10.3px;color:#2f363c}

.exp-item{position:absolute;left:585px;width:360px;height:72px}
.exp-item.alt{background:#e3e7ee}
.exp-thumb{position:absolute;left:8px;top:4px;width:84px;height:56px;border:2px solid #b9c2ca}
.exp-item h4{position:absolute;left:100px;top:2px;font-weight:400;font-size:12.5px;color:#1b2329}
.exp-item p{position:absolute;left:101px;top:20px;width:256px;font-size:10.3px;line-height:12.5px;color:#2b3137}

/* footer */
.foot-rule{left:145px;top:1121px;width:802px;height:1px;background:#6f8f99}
.foot-links{left:0;top:1143px;width:1092px;text-align:center;font-size:10.5px;color:#6a7075;line-height:15.5px}
.foot-links a{color:#6a7075;text-decoration:none}
.foot-links b{font-weight:400;color:var(--ink)}
</style>
</head>
<body>
<div class="top-band"></div>

<header>
  <div class="abs brand"><span class="brand-mark"></span><span class="brand-name">Harlowe Bexley<br>Construction Services</span></div>
  <div class="abs nav-rule"></div>
  <nav class="abs nav">
    <a class="current" href="#">Home</a>
    <a href="#" style="left:93px">About Us</a>
    <a href="#" style="left:183px">Links</a>
    <a href="#" style="left:252px">Free Downloads</a>
    <a href="#" style="left:380px">Careers</a>
    <a href="#" style="left:460px">Contacts</a>
    <div class="abs search">Type search here ...
      <svg width="15" height="13" viewBox="0 0 15 13"><circle cx="5.5" cy="5.5" r="4" fill="none" stroke="#444" stroke-width="1.6"/><line x1="8.5" y1="8.5" x2="13.5" y2="12" stroke="#444" stroke-width="2.2"/></svg>
    </div>
  </nav>
</header>

<div class="abs hero-shadow"></div>
<section class="abs hero" role="img" aria-label="Photograph of a modern glass and steel office building at dusk with people walking near the entrance">
  <div class="service s1"><h3>Construction Management</h3><p>From start to finish; from demolition and site excavation to lock up, council sign off and tax depreciation. Our Project Management process is a detailed <span class="more">+ Read more</span></p></div>
  <div class="service s2"><h3>Project Management</h3><p>From start to finish; from demolition and site excavation to lock up, council sign off and tax depreciation. Our Project Management process is a detailed <span class="more">+ Read more</span></p></div>
  <div class="service s3"><h3>Building</h3><p>From start to finish; from demolition and site excavation to lock up, council sign off and tax depreciation. Our Project Management process is a detailed <span class="more">+ Read more</span></p></div>
  <div class="feature">
    <h1>Deliver the project you want<br>on time, to budget</h1>
    <p>The essence of our business is ensuring every project we undertake achieves the client’s objectives. Our experience has shown the secrets to a profitable project are PLANNING,&nbsp; ATTENTION TO DETAIL, VALUE ADD</p>
    <span class="more">+ Read more</span>
  </div>
</section>

<main>
  <h2 class="abs sec-head welcome-head">Welcome to <b>HARLOWE BEXLEY</b></h2>
  <p class="abs intro">We are a Sydney based Construction Company who can help with all your construction needs. The Harlowe Bexley process helps define your budget, establishes Return on Investment and reduces potential risk.</p>
  <h3 class="abs why" style="font-weight:400">Why Choose Us?</h3>
  <ul class="abs reasons">
    <li><svg width="14" height="12" viewBox="0 0 14 12"><path d="M1 6l4 4 8-9" fill="none" stroke="#6aa63a" stroke-width="2.4"/></svg>Architects – to assist with costing a project, value-engineering and project imple mentation.</li>
    <li><svg width="14" height="12" viewBox="0 0 14 12"><path d="M1 6l4 4 8-9" fill="none" stroke="#6aa63a" stroke-width="2.4"/></svg>Owner/Builders – to assist with project management, costings, work flow and final sign offs</li>
    <li><svg width="14" height="12" viewBox="0 0 14 12"><path d="M1 6l4 4 8-9" fill="none" stroke="#6aa63a" stroke-width="2.4"/></svg>Developers – to assist with costings, tender appraisal and project management</li>
    <li><svg width="14" height="12" viewBox="0 0 14 12"><path d="M1 6l4 4 8-9" fill="none" stroke="#6aa63a" stroke-width="2.4"/></svg>Strata managers – remediation, fire safety</li>
    <li><svg width="14" height="12" viewBox="0 0 14 12"><path d="M1 6l4 4 8-9" fill="none" stroke="#6aa63a" stroke-width="2.4"/></svg>Sub-contractors – for pricing assistance</li>
    <li><svg width="14" height="12" viewBox="0 0 14 12"><path d="M1 6l4 4 8-9" fill="none" stroke="#6aa63a" stroke-width="2.4"/></svg>Lessor and lessees – for fit outs and make good work</li>
    <li><svg width="14" height="12" viewBox="0 0 14 12"><path d="M1 6l4 4 8-9" fill="none" stroke="#6aa63a" stroke-width="2.4"/></svg>Investors – to define profitability, feasibility and risk</li>
    <li><svg width="14" height="12" viewBox="0 0 14 12"><path d="M1 6l4 4 8-9" fill="none" stroke="#6aa63a" stroke-width="2.4"/></svg>Finance companies – risk analysis</li>
    <li><svg width="14" height="12" viewBox="0 0 14 12"><path d="M1 6l4 4 8-9" fill="none" stroke="#6aa63a" stroke-width="2.4"/></svg>Solicitors – advisory services</li>
    <li><svg width="14" height="12" viewBox="0 0 14 12"><path d="M1 6l4 4 8-9" fill="none" stroke="#6aa63a" stroke-width="2.4"/></svg>Construction is a minefield. We’ll help you through it!</li>
  </ul>

  <h2 class="abs sec-head testi-head">Client <b>TESTIMONIALS</b></h2>
  <blockquote class="abs quote">Harlowe Bexley is a construction company with significant skills in Project and Construction Management. We will help you undertake a successful construction.<br><br>“The success of our Newcastle project built our confidence in the ability of Harlowe Bexley.”</blockquote>
  <svg class="abs quote-tail" width="42" height="16" viewBox="0 0 42 16"><path d="M0 0h40v16z" fill="#e4e8ef"/></svg>
  <p class="abs signature">Martin Ashdown Director Kelvar Constructions</p>

  <h2 class="abs sec-head exp-head">Our <b>EXPERIENCE</b></h2>
  <article class="exp-item" style="top:802px">
    <div class="exp-thumb" role="img" aria-label="Interior with pendant light and timber wall panels" style="background:linear-gradient(90deg,#d9dfe0,#b98a5a)"></div>
    <h4>Interior Design</h4><p>Duis autem vel eum iriure dolor in hendrerit in vulputate velit esse molestie consequat, vel illum dolore eu feugiat</p>
  </article>
  <article class="exp-item alt" style="top:878px">
    <div class="exp-thumb" role="img" aria-label="Open living area with timber staircase" style="background:linear-gradient(90deg,#6f5a4c,#c9b9a6,#8a6a4a)"></div>
    <h4>Interior Design</h4><p>Duis autem vel eum iriure dolor in hendrerit in vulputate velit esse molestie consequat, vel illum dolore eu feugiat</p>
  </article>
  <article class="exp-item" style="top:954px">
    <div class="exp-thumb" role="img" aria-label="Glass balustrade staircase in a bright interior" style="background:linear-gradient(160deg,#e6e6e6,#a8a39c 60%,#c9403d)"></div>
    <h4>Interior Design</h4><p>Duis autem vel eum iriure dolor in hendrerit in vulputate velit esse molestie consequat, vel illum dolore eu feugiat</p>
  </article>
  <article class="exp-item" style="top:1030px">
    <div class="exp-thumb" role="img" aria-label="Kitchen and dining room with timber floor" style="background:linear-gradient(180deg,#d8d6d0,#8c7a62)"></div>
    <h4>Interior Design</h4><p>Duis autem vel eum iriure dolor in hendrerit in vulputate velit esse molestie consequat, vel illum dolore eu feugiat</p>
  </article>
</main>

<footer>
  <div class="abs foot-rule"></div>
  <div class="abs foot-links">
    <a href="#">Home</a> | <a href="#">About Us</a> | <a href="#">Building</a> | <a href="#">Construction Management</a> | <a href="#">Project Management</a> | <a href="#">Links</a> | <a href="#">Free Downloads</a> | <a href="#">Careers</a> | <a href="#">Contacts</a><br>
    Copyright © 2008 <b>Harlowe Bexley</b>, All Rights Reserved - Webmaster &nbsp;&nbsp; | &nbsp;&nbsp; <a href="#">Privacy policy</a> &nbsp;&nbsp; | &nbsp;&nbsp; <a href="#">Admint</a>
  </div>
</footer>
</body>
</html>
```